out of the box Business Card Design for a Manufacturer / Distributor

We are a manufarturer and distributor of products.
the company name is VORTANI (Pic attached)

the picture is NOT a must have on the business Card.

the Business Card should look really professional and/or special, so out of the box thinking is welcome.

there should be 2 Adresses on the Business Card for Main and Branch Office.
Email Adress, homepage, Name is required
NO Phone Number

Our working field:
Private Labeling
high Quality Production
direct distribution
warehousing
trademark registration
legal support

Main Office:
Kornblumenweg 14
08352 Ellerbrück
Germany

Branch Office:
Daska Lane
Zerhanpur
Pakistan

Names:
Lukas Feldhaus (Owner)
Imran Qureshi (Owner)

Email:
lukas@vortani-example.com
imran@vortani-example.com

homepage:
vortani-example.com

Industry/Entity Type

Manufacturer Distributer

Contact Information for Business Card

Vortani

Requirements
Must have
• Names, both office Adresses, email, homepage
Should not have
• Phone Number

```html
<!DOCTYPE html>
<html lang="en">
<head>
<meta charset="utf-8">
<title>VORTANI Business Card</title>
<link rel="stylesheet" href="https://fonts.googleapis.com/css2?family=Didact+Gothic&family=Open+Sans:wght@400;600;700&display=swap">
<style>
  :root {
    --backdrop: #8a8a8a;
    --card: #ffffff;
    --ink: #1a1a1a;
    --ink-soft: #3c3c3c;
    --ink-muted: #5a5a5a;
    --band: #0e0e0e;
    --band-text: #ffffff;
    --rule: #c8c8c8;
  }
  * { box-sizing: border-box; margin: 0; padding: 0; }
  html, body {
    width: 1200px;
    height: 876px;
    overflow: hidden;
    background: var(--backdrop);
  }
  .canvas {
    position: relative;
    width: 1200px;
    height: 876px;
    display: flex;
    align-items: center;
    justify-content: center;
    gap: 60px;
  }
  .card {
    position: relative;
    width: 520px;
    height: 292px;
    background: var(--card);
    overflow: hidden;
    box-shadow: 0 6px 18px rgba(0, 0, 0, 0.25);
  }
  .card--back { align-self: flex-start; margin-top: 180px; }
  .card--front { align-self: flex-end; margin-bottom: 180px; }

  .edge-line {
    position: absolute;
    left: 8px; top: 0; bottom: 0;
    width: 6px;
    background: var(--band);
  }
  .edge-band {
    position: absolute;
    left: 20px; top: 0; bottom: 0;
    width: 24px;
    background: var(--band);
    display: flex;
    align-items: center;
    justify-content: center;
  }
  .edge-band__url {
    transform: rotate(-90deg);
    white-space: nowrap;
    font-family: "Open Sans", sans-serif;
    font-size: 9px;
    letter-spacing: 1.6px;
    font-weight: 600;
    color: var(--band-text);
  }

  .wordmark {
    display: flex;
    align-items: center;
    gap: 14px;
  }
  .wordmark__dot {
    width: 22px; height: 22px;
    border-radius: 50%;
    background: var(--ink-soft);
    flex: none;
  }
  .wordmark__name {
    font-family: "Didact Gothic", sans-serif;
    color: var(--ink);
    letter-spacing: 1px;
    line-height: 1;
  }

  /* back side */
  .back__content {
    position: absolute;
    left: 120px; top: 108px;
  }
  .back .wordmark__name { font-size: 52px; }
  .back__url {
    margin-top: 10px;
    margin-left: 36px;
    font-family: "Open Sans", sans-serif;
    font-size: 12px;
    letter-spacing: 4px;
    color: var(--ink-soft);
  }

  /* front side */
  .front__content {
    position: absolute;
    left: 72px; top: 26px; right: 24px;
  }
  .front .wordmark__name { font-size: 40px; }
  .front__services {
    margin-top: 10px;
    font-family: "Open Sans", sans-serif;
    font-size: 10.5px;
    line-height: 1.35;
    color: var(--ink-soft);
  }
  .contacts {
    margin-top: 16px;
    display: flex;
    gap: 22px;
  }
  .contact { flex: 1; }
  .contacts__divider {
    width: 1px;
    background: var(--rule);
    margin-top: 26px;
    height: 56px;
  }
  .contact__name {
    font-family: "Open Sans", sans-serif;
    font-size: 13px;
    color: var(--ink);
  }
  .contact__email {
    margin-top: 4px;
    font-family: "Open Sans", sans-serif;
    font-size: 9.5px;
    color: var(--ink-muted);
  }
  .contact__office {
    margin-top: 10px;
    font-family: "Open Sans", sans-serif;
    font-size: 8.5px;
    font-weight: 700;
    color: var(--ink-soft);
    text-transform: uppercase;
  }
  .contact__address {
    font-family: "Open Sans", sans-serif;
    font-size: 8.5px;
    line-height: 1.4;
    color: var(--ink-muted);
    font-style: normal;
  }
</style>
</head>
<body>
<main class="canvas">
  <section class="card card--front front" aria-label="Business card, front">
    <div class="edge-line"></div>
    <div class="edge-band"><span class="edge-band__url">www.vortani-example.com</span></div>
    <div class="front__content">
      <div class="wordmark">
        <span class="wordmark__dot"></span>
        <span class="wordmark__name">VORTANI</span>
      </div>
      <p class="front__services">Private Labeling | high Quality Production | direct distribution<br>| warehousing | trademark registration | legal support</p>
      <div class="contacts">
        <div class="contact">
          <p class="contact__name">Lukas Feldhaus (Owner)</p>
          <p class="contact__email">lukas@vortani-example.com</p>
          <p class="contact__office">Main Office:</p>
          <address class="contact__address">Kornblumenweg 14<br>08352 Ellerbrück<br>Germany</address>
        </div>
        <div class="contacts__divider"></div>
        <div class="contact">
          <p class="contact__name">Imran Qureshi (Owner)</p>
          <p class="contact__email">imran@vortani-example.com</p>
          <p class="contact__office">Branch Office:</p>
          <address class="contact__address">Daska Lane<br>Zerhanpur<br>Pakistan</address>
        </div>
      </div>
    </div>
  </section>

  <section class="card card--back back" aria-label="Business card, back">
    <div class="edge-line"></div>
    <div class="edge-band"><span class="edge-band__url">www.vortani-example.com</span></div>
    <div class="back__content">
      <div class="wordmark">
        <span class="wordmark__dot"></span>
        <span class="wordmark__name">VORTANI</span>
      </div>
      <p class="back__url">www.vortani-example.com</p>
    </div>
  </section>
</main>
</body>
</html>
```